KT Prime Motion personal training needs a new Business Card design for 2016

Business Card design:
Our current business card is very plain
We are bringing on our first team member next year and thought its a perfect time to have a new face lift for our company!

We are a Personal Training business "KT Prime Motion" who specializes in strength and conditioning / weightloss training,
We also run a yearly Bootcamp called "Ferocity Drillcamps", this is our Logo Design which we are looking for

The pink and blue in the logo are our business colours, how ever we don't want those colours to heavily dominate the card.

We are looking for a business card which is eye catching, and creative.

I am open to suggestions and any designs :)

Logo Design:

For our Logo Design we are looking for a bright, energetic logo, preferably a word logo which portrays strength and high intensity
If it has icon's etc in it thats fine again im open for suggestions :)
The Logo Design is for our Bootcamp which runs yearly
The bootcamp is called "Ferocity Drillcamp"

Target Market(s)

Age 20-40
Individuals who want to look great and have more energy

Industry/Entity Type

Business

Contact Information for Business Card

On the front
KT Prime Motion Doriel Maxton Personal Training / Bootcamps / Pilates / Nutrition Healthy mind, Healthy body, Ultimate lifestyle < our slogan
Icons for the following
Email:
Mobile:
Facebook:
Instagram:

On the back we would like to include somewhere
"Show this card to receive 50% off your first 30min pt session"
"Valid to one user only"

Logo Text

Ferocity Drillcamp

Font styles to use
Serif

Colors
e34197
0255a3
000000
ffffff

Requirements
Must have
• - Icons for instagram, facebook, email and mobile phone
• - Slogan: Healthy mind, Healthy body, Ultimate lifestyle
• - What we offer: Personal Training , Bootcamps, Pilates, Nutrition
• - Logo
• -
Nice to have
• - Our 50% offer on the back
• - a place for a photo
Should not have
• - Pink and Blue everywhere

```html
<!DOCTYPE html>
<html lang="en">
<head>
<meta charset="utf-8">
<title>KT Prime Motion – Business Card</title>
<link href="https://fonts.googleapis.com/css2?family=Bebas+Neue&family=Roboto+Condensed:wght@400;700&display=swap" rel="stylesheet">
<style>
  :root{
    --pink:#e34197;
    --pink-soft:#f0a3cb;
    --blue:#0255a3;
    --blue-card:#4a78d2;
    --blue-light:#7ea3ea;
    --black:#111111;
    --white:#ffffff;
    --grey:#555555;
    --stage:#ecebe8;
  }
  *{box-sizing:border-box;margin:0;padding:0}
  html,body{width:1200px;height:1000px;overflow:hidden;background:var(--stage)}
  .canvas{position:relative;width:1200px;height:1000px}
  .card{
    position:absolute;left:220px;width:760px;height:464px;
    overflow:hidden;border-radius:4px;
    box-shadow:0 6px 18px rgba(0,0,0,.18);
  }
  /* ---------- back of card ---------- */
  .card-back{top:24px;background:var(--blue-card);color:var(--white);text-align:center}
  .card-back .texture{
    position:absolute;inset:0;
    background:
      radial-gradient(ellipse at 80% 10%, rgba(255,255,255,.25), transparent 55%),
      linear-gradient(160deg, var(--blue-light) 0%, var(--blue-card) 45%, #3b63c0 100%);
  }
  .back-content{position:relative;padding-top:46px}
  .brand{
    display:inline-flex;align-items:center;gap:12px;
    font-family:"Bebas Neue",sans-serif;font-size:40px;letter-spacing:1px;line-height:1;
  }
  .brand-dot{width:34px;height:34px;border-radius:50%}
  .card-back .brand{color:var(--white)}
  .card-back .brand-dot{background:var(--white)}
  .offer-intro{
    margin-top:34px;font-family:"Bebas Neue",sans-serif;font-size:50px;letter-spacing:1px;line-height:1;
  }
  .offer-value{
    font-family:"Bebas Neue",sans-serif;font-size:150px;line-height:.9;color:var(--pink);
  }
  .offer-detail{
    font-family:"Bebas Neue",sans-serif;font-size:46px;letter-spacing:1px;line-height:1;
  }
  .offer-terms{
    margin-top:14px;font-family:"Roboto Condensed",sans-serif;font-style:italic;font-size:22px;letter-spacing:1px;
  }
  /* ---------- front of card ---------- */
  .card-front{top:512px;background:var(--white)}
  .top-band{position:absolute;left:0;top:0;width:100%;height:12px;background:var(--blue-card)}
  .pink-wash{
    position:absolute;right:0;bottom:0;width:100%;height:100%;
    background:linear-gradient(120deg, transparent 0%, transparent 62%, var(--pink-soft) 78%, var(--pink) 100%);
    clip-path:polygon(60% 100%,100% 40%,100% 100%);
  }
  .divider{position:absolute;left:0;top:0;width:100%;height:100%}
  .front-logo{position:absolute;left:56px;top:196px}
  .front-logo .brand{font-size:46px;color:var(--blue)}
  .front-logo .brand-dot{background:var(--pink);width:40px;height:40px}
  .details{position:absolute;left:380px;top:48px;width:360px}
  .person-name{
    font-family:"Bebas Neue",sans-serif;font-size:64px;line-height:1;color:var(--black);letter-spacing:1px;
  }
  .services{
    margin-top:6px;font-family:"Bebas Neue",sans-serif;font-size:23px;line-height:1.08;letter-spacing:.5px;
  }
  .services .pink{color:var(--pink)}
  .services .blue{color:var(--blue)}
  .contacts{list-style:none;margin-top:22px}
  .contacts li{
    display:flex;align-items:center;gap:10px;margin-bottom:9px;
    font-family:"Roboto Condensed",sans-serif;font-size:16px;color:var(--grey);
  }
  .contacts svg,.contacts .social-mark{width:20px;height:20px;flex:none}
  .social-mark{display:inline-block;background:var(--grey);border-radius:3px}
</style>
</head>
<body>
<main class="canvas">

  <section class="card card-back" aria-label="Business card back">
    <div class="texture" role="img" aria-label="Soft blue abstract swirl background"></div>
    <div class="back-content">
      <div class="brand"><span class="brand-dot"></span>KT Prime Motion</div>
      <p class="offer-intro">Show this card to receive</p>
      <p class="offer-value">50% OFF</p>
      <p class="offer-detail">Your first 30min PT session</p>
      <p class="offer-terms">*Valid to one user only*</p>
    </div>
  </section>

  <section class="card card-front" aria-label="Business card front">
    <div class="top-band"></div>
    <div class="pink-wash" role="img" aria-label="Pink brush-streak texture in the corner"></div>
    <svg class="divider" viewBox="0 0 760 464" preserveAspectRatio="none" aria-hidden="true">
      <line x1="350" y1="40" x2="350" y2="330" stroke="#dddddd" stroke-width="1.5"/>
    </svg>

    <div class="front-logo">
      <div class="brand"><span class="brand-dot"></span>KT Prime Motion</div>
    </div>

    <div class="details">
      <h1 class="person-name">Doriel Maxton</h1>
      <p class="services">
        <span class="pink">Personal Training / </span><span class="blue">Bootcamps /</span><br>
        <span class="blue">Pilates / </span><span class="pink">Nutrition </span><span class="blue">Healthy Mind,</span><br>
        <span class="pink">Healthy Body. </span><span class="blue">Ultimate Lifestyle</span>
      </p>
      <ul class="contacts">
        <li>
          <svg viewBox="0 0 20 20" aria-hidden="true"><rect x="1" y="4" width="18" height="12" rx="1.5" fill="#555"/><path d="M2 5l8 6 8-6" stroke="#fff" stroke-width="1.5" fill="none"/></svg>
          hello@ktprimemotion.com
        </li>
        <li>
          <svg viewBox="0 0 20 20" aria-hidden="true"><path d="M5 2h3l1.5 4-2 1.5a10 10 0 0 0 5 5l1.5-2 4 1.5v3a2 2 0 0 1-2 2A15 15 0 0 1 3 4a2 2 0 0 1 2-2z" fill="#555"/></svg>
          0400 317 562
        </li>
        <li><span class="social-mark" aria-hidden="true"></span>/ktprimemotion</li>
        <li><span class="social-mark" aria-hidden="true"></span>/dorielmaxton_pt</li>
      </ul>
    </div>
  </section>

</main>
</body>
</html>
```